PerkHaven.com.au Web Redesign

We need a web redesign for our existing website at http://perkhaven.com.au. Our website hosts a registration form for users who are interested in surveys, samples/trials, competitions (contests), and freebie offers. We rely heavily on emails as our main tool to communicate with our users. The current theme of our website is really white and bright. We would like to see a rather bold but playful theme like red, orange, and dark grey. The final design should be able to: 1) entice users to register; 2) look fun & playful; 3) have the modern, but colorful touch; and 4) present the theme of the offers (i.e. Tarlo, Brisk/Pinemarket, and Harlow Vance gift cards). The current logo can be redesigned into a new logo to suit the new web design.
Updates

Your new design must cover the following pages:

/index.html
/catalogue.html
/confirm-your-subscription.html
/contact-us.html
/daily-deals.html
/faqs.html
/terms-of-use.html
/thank-you.html

I missed out two extra pages that should be included in this project

/restaurant.html
/travel.html

Project Deadline Extended
Reason: Deadline is now extended by 15 more days. This should give you more time to be creative.

Target Market(s)

Age 18-65, both males & females, any occupations.

Requirements
Must have
• The new design must have the corresponding theme of the offer presented (Tarlo, BRISK/Pinemarket, and Harlow Vance).
Nice to have
• The current layout of our website crams all 3 gift card offers into one page. Feel free to redesign the website into 3 different pages with each page containing a dedicated offer. This will enhance the theme of the offer presented.

```html
<!DOCTYPE html>
<html lang="en">
<head>
<meta charset="utf-8">
<title>Perk Haven – Bringing Aussie's Best Rewards To You</title>
<link href="https://fonts.googleapis.com/css2?family=PT+Sans+Narrow:wght@400;700&family=Open+Sans:wght@400;600&display=swap" rel="stylesheet">
<style>
:root{
  --red:#d7121a;
  --red-dark:#a8060d;
  --orange:#fdab00;
  --orange-dark:#e69a00;
  --slate:#2f3e4b;
  --slate-dark:#1d2730;
  --ink:#2a3a48;
  --text:#666;
  --line:#dcdcdc;
  --footer:#f3f3f3;
}
*{box-sizing:border-box;margin:0;padding:0}
html,body{width:820px;height:1200px;overflow:hidden;background:#fff}
body{position:relative;font-family:"Open Sans",Arial,sans-serif;color:var(--text)}
.narrow{font-family:"PT Sans Narrow",Arial Narrow,sans-serif}

/* header */
.site-header{position:absolute;left:0;top:0;width:820px;height:86px}
.brand{position:absolute;left:42px;top:27px}
.brand-name{font-family:"PT Sans Narrow",sans-serif;font-weight:700;font-size:32px;line-height:30px;color:var(--red)}
.brand-tag{font-size:8px;letter-spacing:.4px;color:#555;margin-top:2px}
.main-nav{position:absolute;right:38px;top:41px;display:flex;align-items:center;font-family:"PT Sans Narrow",sans-serif;font-weight:700;font-size:14px;color:var(--ink)}
.main-nav a{color:inherit;text-decoration:none;padding:0 9px;border-left:1px solid #bbb;line-height:14px}
.main-nav a.first{border:none}
.main-nav a.active{background:var(--red);color:#fff;padding:6px 15px;border:none;border-radius:2px;margin-right:0}

/* hero */
.hero{position:absolute;left:0;top:86px;width:820px;height:338px;background:linear-gradient(#3a4753,#2c3843)}
.hero-frame{position:absolute;left:31px;top:6px;width:758px;height:320px;background:#55616c;border-radius:3px}
.hero-panel{position:absolute;left:7px;top:5px;width:744px;height:309px;background:#fff;border-radius:3px;overflow:hidden}
.hero-photo{position:absolute;left:0;top:0;width:490px;height:309px;background:linear-gradient(120deg,#e9edf2 0%,#f7f1ea 45%,#efd9b8 70%,#fafafa 100%)}
.register{position:absolute;left:492px;top:12px;width:240px;height:285px;border:2px solid #ececec;border-radius:3px;padding:14px 20px}
.register h2{font-family:"PT Sans Narrow",sans-serif;font-weight:700;font-size:22px;color:var(--ink);margin-bottom:8px}
.field{height:25px;border:1px solid #dedede;font-size:10px;color:#555;padding:6px 11px;margin-bottom:7px;background:#fff}
.field-row{display:flex;gap:5px}
.field-row .field{flex:1}
.consent{font-size:8.4px;line-height:14px;color:#777;margin:2px 0 10px}
.submit{display:inline-block;background:var(--red);color:#fff;font-family:"PT Sans Narrow",sans-serif;font-weight:700;font-size:12px;padding:5px 13px;border-radius:3px}

/* promo banner */
.promo{position:absolute;left:31px;top:450px;width:758px;height:130px;color:#fff;text-align:center}
.promo svg{position:absolute;left:0;top:0}
.promo-inner{position:relative;padding-top:18px}
.promo h1{font-family:"PT Sans Narrow",sans-serif;font-weight:700;font-size:24px;margin-bottom:4px}
.promo p{font-family:"PT Sans Narrow",sans-serif;font-size:13px;line-height:18.5px;padding:0 66px}

/* gift cards */
.gift-card{position:absolute;top:608px;width:244px;height:133px;border-radius:3px;overflow:hidden;color:#fff}
.gift-card h3{position:absolute;left:23px;top:16px;font-family:"PT Sans Narrow",sans-serif;font-weight:700;font-size:23px}
.perks{position:absolute;left:23px;top:50px;list-style:none;font-family:"PT Sans Narrow",sans-serif;font-size:13px}
.perks li{display:flex;align-items:center;gap:4px;height:21px}
.gift-circle{position:absolute;left:141px;top:38px;width:122px;height:122px;border-radius:50%;text-align:center}
.gift-circle .amount{display:block;margin:15px 0 0 -18px;font-family:"PT Sans Narrow",sans-serif;font-weight:700;font-size:34px;line-height:34px}
.gift-circle .label{display:block;margin-left:-18px;font-family:"PT Sans Narrow",sans-serif;font-size:13px}
.card-red{left:31px;background:var(--red)} .card-red .gift-circle{background:var(--red-dark)}
.card-orange{left:284px;background:var(--orange)} .card-orange .gift-circle{background:var(--orange-dark)}
.card-slate{left:535px;background:var(--slate)} .card-slate .gift-circle{background:var(--slate-dark)}

/* info */
.section-title{position:absolute;font-family:"PT Sans Narrow",sans-serif;font-weight:700;color:var(--ink);font-size:21px}
.info-box{position:absolute;top:834px;width:240px;height:220px;border:1px solid #d8d8d8;border-radius:3px;padding:16px 17px}
.info-box h4{font-family:"PT Sans Narrow",sans-serif;font-weight:700;font-size:19px;color:var(--red);margin-bottom:6px}
.info-box p{font-size:9.6px;line-height:16.3px;color:#777;margin-bottom:8px}
.learn{position:absolute;left:17px;bottom:18px;font-family:"PT Sans Narrow",sans-serif;font-weight:700;font-size:12px;color:var(--red)}
.why{position:absolute;left:563px;top:840px;width:193px;list-style:none}
.why li{height:26px;border-bottom:1px solid #e6e6e6;font-family:"PT Sans Narrow",sans-serif;font-size:12px;color:var(--ink);display:flex;align-items:center;gap:6px}

/* footer */
.site-footer{position:absolute;left:0;top:1090px;width:820px;height:110px;background:linear-gradient(#f4f4f4,#fff)}
.footer-links{position:absolute;left:44px;top:27px;font-size:10px;color:var(--ink)}
.footer-links span{padding:0 5px;color:#555}
.copyright{position:absolute;left:44px;top:51px;font-size:8.5px;color:#555}
.social{position:absolute;left:692px;top:22px;display:flex;gap:7px}
.social i{width:20px;height:20px;border-radius:50%;background:#8a8f94;display:block}
</style>
</head>
<body>

<header class="site-header">
  <div class="brand">
    <div class="brand-name">Perk Haven</div>
    <div class="brand-tag">BRINGING AUSSIE'S BEST REWARDS TO YOU</div>
  </div>
  <nav class="main-nav">
    <a class="active">MAIN</a>
    <a class="first">COMPETITIONS</a>
    <a>SURVEYS</a>
    <a>FREEBIES</a>
    <a>FAQ</a>
    <a>ABOUT US</a>
    <a>TERM OF USE</a>
  </nav>
</header>

<section class="hero">
  <div class="hero-frame">
    <div class="hero-panel">
      <div class="hero-photo" role="img" aria-label="Photo of a woman typing on a laptop on a white bed"></div>
      <form class="register">
        <h2>Register Here!</h2>
        <div class="field">First name</div>
        <div class="field">Last Name</div>
        <div class="field">Email address</div>
        <div class="field-row"><div class="field">Male</div><div class="field">Year of Birth</div></div>
        <div class="field-row"><div class="field">Suburb</div><div class="field">Post Code</div></div>
        <p class="consent">By ticking this box, you agree to subscribe to our newsletter and accept our Terms of Us</p>
        <span class="submit">SUBMIT NOW</span>
      </form>
    </div>
  </div>
</section>

<section class="promo">
  <svg width="758" height="130" viewBox="0 0 758 130">
    <defs><linearGradient id="promoFill" x1="0" y1="0" x2="0" y2="1"><stop offset="0" stop-color="#cf0d14"/><stop offset="1" stop-color="#9a050b"/></linearGradient></defs>
    <path d="M3 0H755Q758 0 758 3V112Q379 136 0 112V3Q0 0 3 0Z" fill="url(#promoFill)"/>
  </svg>
  <div class="promo-inner">
    <h1>Win a $500 Gift Card of Your Choice Every Month!</h1>
    <p>Mauris vel lacus vitae felis vestibulum volutpat. Etiam est nunc, venenatis in, tristique eu, imperdiet ac, nisl. Cum sociis natoque penatibus et magnis dis parturient montes, nascetur ridiculus mus. In iaculis facilisis massa. Etiam eu urna. Sed porta. Suspendisse quam leo, molestie sed, luctus quis, feugiat in, pede. Fusce tellus. Sed metus augue, convallis et, vehicula ut, pulvinar eu, ante</p>
  </div>
</section>

<svg width="0" height="0" style="position:absolute">
  <symbol id="tick" viewBox="0 0 12 10"><path d="M1 5.5L4.3 8.5L11 1.5" fill="none" stroke="currentColor" stroke-width="2.2" stroke-opacity=".75"/></symbol>
  <symbol id="caret" viewBox="0 0 6 8"><path d="M0 0L5 4L0 8Z" fill="currentColor"/></symbol>
</svg>

<article class="gift-card card-red">
  <h3>TARLO &amp; KESTREL</h3>
  <ul class="perks">
    <li><svg width="12" height="10"><use href="#tick"/></svg>Lots of Stores</li>
    <li><svg width="12" height="10"><use href="#tick"/></svg>Millions of Gifts</li>
    <li><svg width="12" height="10"><use href="#tick"/></svg>Maximum Choice</li>
  </ul>
  <div class="gift-circle"><span class="amount">$500</span><span class="label">Gift Card <svg width="5" height="7"><use href="#caret"/></svg></span></div>
</article>
<article class="gift-card card-orange">
  <h3>BRISK</h3>
  <ul class="perks">
    <li><svg width="12" height="10"><use href="#tick"/></svg>Perfect Gift</li>
    <li><svg width="12" height="10"><use href="#tick"/></svg>Buy Anything</li>
    <li><svg width="12" height="10"><use href="#tick"/></svg>Choice of Stories</li>
  </ul>
  <div class="gift-circle"><span class="amount">$500</span><span class="label">Gift Card <svg width="5" height="7"><use href="#caret"/></svg></span></div>
</article>
<article class="gift-card card-slate">
  <h3>HARLOW VANCE</h3>
  <ul class="perks">
    <li><svg width="12" height="10"><use href="#tick"/></svg>World of Choice</li>
    <li><svg width="12" height="10"><use href="#tick"/></svg>Finest Brands</li>
    <li><svg width="12" height="10"><use href="#tick"/></svg>Wonderful Gifts</li>
  </ul>
  <div class="gift-circle"><span class="amount">$500</span><span class="label">Gift Card <svg width="5" height="7"><use href="#caret"/></svg></span></div>
</article>

<h2 class="section-title" style="left:34px;top:794px">Australia's Leading Source of Online Competition &amp; Surveys</h2>
<h2 class="section-title" style="left:561px;top:794px">Why Subscribe?</h2>

<div class="info-box" style="left:36px">
  <h4>Rewarding Offer Only</h4>
  <p>At Perk Haven, we bring you the most popular competitions, surveys, freebies, and various samples and trials so that you can maximize your chance to be rewarded. Simply sign up with us and enter the chance to win our monthly $500 gift cards of your choice. This is just the beginning of the most rewarding experience..</p>
  <span class="learn">Learn More <svg width="5" height="7"><use href="#caret"/></svg></span>
</div>
<div class="info-box" style="left:284px">
  <h4>It is always FREE!</h4>
  <p>By signing up, you will receive our weekly exclusive offers which are available to our members only. Registration is 100% free!</p>
  <p>You pay no fees, no subscriptions, no credit cards, and no hassles from telemarketers. We present you with the offers in your e-mail, you simply choose the ones that interest you.</p>
  <span class="learn">Learn More <svg width="5" height="7"><use href="#caret"/></svg></span>
</div>

<ul class="why">
  <li><svg width="5" height="8" style="color:var(--ink)"><use href="#caret"/></svg>Free Registration</li>
  <li><svg width="5" height="8" style="color:var(--ink)"><use href="#caret"/></svg>Greater Chance to Win</li>
  <li><svg width="5" height="8" style="color:var(--ink)"><use href="#caret"/></svg>Privacy Protection</li>
  <li><svg width="5" height="8" style="color:var(--ink)"><use href="#caret"/></svg>Monthly Winning Draw</li>
  <li><svg width="5" height="8" style="color:var(--ink)"><use href="#caret"/></svg>No Credit Card Required</li>
  <li><svg width="5" height="8" style="color:var(--ink)"><use href="#caret"/></svg>Exclusive Online Offers</li>
  <li style="border:none"><svg width="5" height="8" style="color:var(--ink)"><use href="#caret"/></svg>Easy to Unsubscribe</li>
</ul>

<footer class="site-footer">
  <div class="footer-links">PRIVACY POLICY<span>|</span>FAQS<span>|</span>ABOUT US<span>|</span>CONTACT US<span>|</span>TERMS OF USE</div>
  <div class="copyright">© 2013 Company Name.&nbsp; All right reserved.&nbsp; Term of Use</div>
  <div class="social"><i></i><i></i><i></i></div>
</footer>

</body>
</html>
```